Santa Flyer/emailable

It's still 6 months until the big night but Santa books up fast!
To make sure all of your good little girls and boys make it onto Santa's Nice list...email or call today to ensure that the real Santa will be at your party for 2013

Santa is real alright.....
He will be dressed all in fur, from his head to his foot,
But his clothes won't be tarnished with ashes and soot.
A bundle of Toys he he can have flung on his back,
And he will looked like a peddler, just opening his pack.

His eyes-how they twinkle! his dimples how merry!
His cheeks are like roses, his nose like a cherry!
His droll little mouth was drawn up like a bow,
And his real beard is as white as the snow.

He has a broad face and a little round belly,
That shakes when he laughs, like a bowlful of jelly!

Call 612-487-5930 or email santa@frostlanehelpers.com
to secure the real Santa for your party!

Private, Corporate, Business promotions, skating parties, etc

Requirements
Nice to have
• Id like it to look old school....like 1950's esque

I included a bunch of photos to use if you wish...maybe some could be faded as a back ground? Not sure.... also included my logo

a tag line could be
Frostlane Helpers...when only the real guy will do
or
'We know Santa"

```html
<!DOCTYPE html>
<html lang="en">
<head>
<meta charset="utf-8">
<title>Frostlane Helpers – Book the Real Santa</title>
<link rel="stylesheet" href="https://fonts.googleapis.com/css2?family=Rye&family=Mountains+of+Christmas:wght@700&family=Roboto+Condensed:ital,wght@1,400&display=swap">
<style>
  :root{
    --lime:#d6dc3c;
    --lime-dark:#b7bd22;
    --frame-red:#c42f3c;
    --panel:#8e9a82;
    --panel-deep:#6f7c66;
    --sepia-light:#c4b49a;
    --sepia-dark:#6e5c48;
    --headline:#d8283a;
    --ink:#111111;
    --white:#ffffff;
  }
  *{margin:0;padding:0;box-sizing:border-box}
  html,body{width:933px;height:1200px;overflow:hidden;background:var(--lime)}
  .flyer{
    position:relative;width:933px;height:1200px;overflow:hidden;
    background:radial-gradient(circle at 30% 40%,var(--lime) 0%,var(--lime-dark) 100%);
  }
  .frame{
    position:absolute;left:24px;top:27px;width:896px;height:1146px;
    background:var(--frame-red);transform:rotate(-0.4deg);
  }
  .panel{
    position:absolute;left:53px;top:53px;width:840px;height:1094px;
    background:radial-gradient(ellipse at 60% 55%,var(--panel) 0%,var(--panel-deep) 100%);
  }
  .photo-fade{
    position:absolute;left:53px;top:53px;width:540px;height:380px;
    background:linear-gradient(160deg,var(--sepia-dark) 0%,var(--sepia-light) 55%,rgba(142,154,130,0) 100%);
    opacity:.8;
  }
  .headline{
    position:absolute;left:140px;top:165px;width:780px;
    font-family:"Rye",serif;font-weight:400;font-size:50px;line-height:58px;
    color:var(--headline);text-align:center;text-transform:uppercase;white-space:nowrap;
    text-shadow:4px 4px 0 var(--ink),-1px -1px 0 var(--ink),1px -1px 0 var(--ink),-1px 1px 0 var(--ink);
    transform:rotate(-4deg);
  }
  .poem{
    position:absolute;left:73px;top:336px;width:720px;
    font-family:"Mountains of Christmas",cursive;font-weight:700;
    font-size:24px;line-height:31px;color:var(--white);white-space:nowrap;
  }
  .poem p{margin-bottom:31px}
  .nice-list{
    position:absolute;left:557px;top:436px;width:362px;height:270px;
    background:var(--ink);border-radius:34px;
    padding:24px 22px 20px 18px;
    font-family:"Mountains of Christmas",cursive;font-weight:700;
    font-size:23px;line-height:30px;color:var(--white);
  }
  .brand{
    position:absolute;left:60px;top:1080px;width:290px;
    font-family:"Mountains of Christmas",cursive;font-weight:700;
    font-size:30px;line-height:36px;color:var(--white);
  }
  .contact{
    position:absolute;left:393px;top:968px;width:520px;
    font-family:"Roboto Condensed",sans-serif;font-style:italic;
    font-size:27px;line-height:36px;color:var(--white);white-space:nowrap;
  }
  .services{
    position:absolute;left:349px;top:1106px;width:560px;
    font-family:"Roboto Condensed",sans-serif;font-style:italic;
    font-size:23px;color:var(--white);white-space:nowrap;
  }
</style>
</head>
<body>
<main class="flyer">
  <div class="frame"></div>
  <div class="panel"></div>
  <div class="photo-fade" role="img" aria-label="Faded sepia photo of a little girl with Santa holding a candy cane"></div>

  <h1 class="headline">It's still 6 months until<br>the big night but Santa<br>books up fast!</h1>

  <section class="poem">
    <p>Santa is real alright.....<br>He will be dressed all in fur,<br>from his head to his foot,<br>But his clothes won't be<br>tarnished with ashes and soot.<br>A bundle of Toys he he can have<br>flung on his back,<br>And he will looked like a peddler,<br>just opening his pack.</p>
    <p>His eyes-how they twinkle! his<br>dimples how merry!<br>His cheeks are like roses, his<br>nose like a cherry!<br>His droll little mouth was drawn up like<br>a bow,<br>And his real beard is as white as the snow.</p>
    <p>He has a broad face and a little round belly,<br>That shakes when he laughs, like a bowlful of jelly!</p>
  </section>

  <aside class="nice-list">To make sure all of your good little girls and boys make it onto Santa's Nice list...email or call today to ensure that the real Santa will be at your party for 2013</aside>

  <p class="brand">Frostlane Helpers</p>

  <p class="contact">Call 612-487-5930 or<br>email santa@frostlanehelpers.com<br>to secure the real Santa for your party!</p>
  <p class="services">Private, Corporate, Business promotions, skating parties, etc</p>
</main>
</body>
</html>
```